Business Card Design Project

Need business card for new non profit organization that includes the attached logo in some form.
with this information
Name: Michael Dorrance Pilbeam
Title: President & Founder
A: P.O. Box 51607, Portland, Oregon, 97214-5160
E: mike@dorrancetrust.org
E: mike@mikepilbeam.com
P: 1.971.555.0172

Industry/Entity Type
Non Profit

```html
<!DOCTYPE html>
<html lang="en">
<head>
<meta charset="utf-8">
<title>Dorrance Trust – Business Card</title>
<link rel="stylesheet" href="https://fonts.googleapis.com/css2?family=Arimo:wght@400;700&family=Nunito:wght@900&display=swap">
<style>
  :root {
    --backdrop: #8f8f8f;
    --card: #ffffff;
    --card-shade: #f1f2f4;
    --navy: #0f2a86;
    --navy-deep: #0a1f6e;
  }
  html, body {
    margin: 0;
    width: 1200px;
    height: 910px;
    overflow: hidden;
    background: var(--backdrop);
  }
  .card {
    position: absolute;
    left: 100px;
    top: 169px;
    width: 1000px;
    height: 572px;
    background: linear-gradient(160deg, var(--card) 0%, var(--card) 55%, var(--card-shade) 100%);
    box-shadow: 0 6px 18px rgba(0,0,0,0.25);
    overflow: hidden;
  }
  .card__bands {
    position: absolute;
    inset: 0;
    width: 100%;
    height: 100%;
  }
  .brand {
    position: absolute;
    left: 70px;
    top: 120px;
    display: flex;
    align-items: center;
    gap: 14px;
  }
  .brand__mark {
    width: 34px;
    height: 34px;
    border-radius: 50%;
    background: var(--navy);
  }
  .brand__name {
    font-family: "Arimo", Arial, sans-serif;
    font-weight: 700;
    font-size: 34px;
    color: var(--navy);
    letter-spacing: 0.5px;
  }
  .contact {
    position: absolute;
    right: 80px;
    top: 255px;
    width: 440px;
    text-align: center;
    color: var(--navy);
    font-family: "Arimo", Arial, sans-serif;
  }
  .contact__name {
    margin: 0;
    font-family: "Nunito", "Arial Rounded MT Bold", sans-serif;
    font-weight: 900;
    font-size: 31px;
    line-height: 1.1;
    padding-bottom: 4px;
    border-bottom: 2px solid var(--navy);
    white-space: nowrap;
  }
  .contact__title {
    margin: 6px 0 18px;
    font-weight: 700;
    font-size: 18px;
  }
  .contact__line {
    margin: 0;
    font-weight: 700;
    font-size: 15.5px;
    line-height: 1.3;
    white-space: nowrap;
  }
</style>
</head>
<body>
  <article class="card">
    <svg class="card__bands" viewBox="0 0 1000 572" preserveAspectRatio="none" aria-hidden="true">
      <!-- top swoosh -->
      <path d="M0 60 C 300 30, 700 10, 1000 0 L 1000 26 C 720 30, 380 44, 0 66 Z" fill="var(--navy)"/>
      <path d="M420 44 C 640 36, 820 30, 1000 28 L 1000 50 C 840 42, 640 44, 420 44 Z" fill="var(--navy)"/>
      <path d="M760 46 C 860 44, 940 44, 1000 46 L 1000 58 C 930 52, 850 50, 760 46 Z" fill="var(--navy)"/>
      <!-- bottom swoosh -->
      <path d="M0 470 C 300 478, 650 458, 1000 418 L 1000 572 L 0 572 Z" fill="var(--navy)"/>
      <path d="M0 482 C 320 486, 660 468, 1000 430 L 1000 440 C 660 480, 320 498, 0 494 Z" fill="var(--card)"/>
      <path d="M0 520 C 340 520, 680 490, 1000 452 L 1000 458 C 680 498, 340 530, 0 530 Z" fill="var(--card)"/>
      <path d="M0 466 C 200 474, 300 474, 420 472 L 0 476 Z" fill="var(--card)"/>
    </svg>

    <div class="brand">
      <span class="brand__mark"></span>
      <span class="brand__name">Dorrance Trust</span>
    </div>

    <section class="contact">
      <h1 class="contact__name">Michael Dorrance Pilbeam</h1>
      <p class="contact__title">President &amp; Founder</p>
      <p class="contact__line">P.O. Box 51607, Portland, Oregon, 97214-5160</p>
      <p class="contact__line">mike@dorrancetrust.org / mike@mikepilbeam.com</p>
      <p class="contact__line">1.971.555.0172</p>
    </section>
  </article>
</body>
</html>
```